Stationery & Business Card Design Project

We require our stationary to be professional, which will stand out but also be sophisticated and reputable.

We also require the following:

* Business card must be double sided
* Logo must stand out with brightfund colours used. Other colours may be added but only in small doses as not to overtake the main colours.
* For business card brightfund pty ltd smsf specialists with administrators at bottom left on the front of the card and details on the back

Industry/Entity Type

Business

Requirements
Must have
• * Business Cards
* With compliments slips –2 different ones
* Forwarding mail slip (smaller version of a with compliments slip)

```html
<!DOCTYPE html>
<html lang="en">
<head>
<meta charset="utf-8">
<title>brightfund stationery</title>
<link href="https://fonts.googleapis.com/css2?family=Arimo:ital,wght@0,400;0,700;1,400&display=swap" rel="stylesheet">
<style>
  :root {
    --navy: #2f2b7c;
    --grey: #6f6f72;
    --grey-light: #d9d9de;
    --ink: #222;
    --paper: #ffffff;
    --backdrop: #e6e6e9;
  }
  * { margin: 0; padding: 0; box-sizing: border-box; }
  html, body { width: 1200px; height: 800px; overflow: hidden; }
  body {
    background: var(--backdrop);
    font-family: "Arimo", Arial, sans-serif;
    color: var(--grey);
    position: relative;
  }
  .sheet {
    position: absolute;
    background: var(--paper);
    overflow: hidden;
    box-shadow: 0 2px 6px rgba(0,0,0,.25);
  }
  .brand { display: flex; align-items: center; gap: 7px; position: absolute; }
  .brand-square { background: var(--navy); flex: none; }
  .brand-name { color: var(--grey); font-weight: 400; letter-spacing: -0.5px; line-height: 1; }
  .brand-tagline { font-size: 6px; letter-spacing: 2px; color: var(--grey); margin-top: 2px; }
  .contact { position: absolute; text-align: right; line-height: 1.45; color: var(--grey); }
  .contact b { color: var(--navy); }
  .big-word {
    position: absolute;
    font-weight: 400;
    line-height: 1;
    letter-spacing: -4px;
    white-space: nowrap;
  }

  /* Letterhead */
  .letterhead { left: 304px; top: 47px; width: 501px; height: 707px; }
  .letterhead .brand { left: 15px; top: 14px; }
  .letterhead .brand-square { width: 32px; height: 32px; }
  .letterhead .brand-name { font-size: 25px; }
  .letterhead .contact { right: 28px; top: 26px; font-size: 9px; }
  .letterhead .big-word { left: -4px; bottom: -18px; font-size: 112px; color: var(--navy); }

  /* Business card front */
  .card-front { left: 152px; top: 183px; width: 242px; height: 135px; }
  .card-front .panel-navy { position: absolute; left: 0; top: 0; width: 60px; height: 112px; background: var(--navy); }
  .card-front .panel-grey { position: absolute; left: 90px; top: 0; width: 152px; height: 64px; background: var(--grey); }
  .card-front .entity { position: absolute; right: 11px; top: 90px; text-align: right; font-size: 8px; font-style: italic; line-height: 1.4; color: var(--grey); }
  .card-front .entity b { color: var(--grey); }
  .card-front .big-word { left: 0; bottom: -9px; font-size: 38px; color: var(--grey-light); letter-spacing: -1px; }

  /* Business card back */
  .card-back { left: 242px; top: 300px; width: 240px; height: 133px; }
  .card-back .brand { left: 6px; top: 16px; }
  .card-back .brand-square { width: 26px; height: 26px; }
  .card-back .brand-name { font-size: 21px; }
  .card-back .person { position: absolute; right: 12px; top: 63px; text-align: right; }
  .person-name { color: var(--ink); font-size: 12px; }
  .person-role { color: var(--grey); font-size: 8px; }
  .card-back .contact { right: 8px; top: 104px; font-size: 6.5px; }

  /* With compliments slip */
  .slip { left: 550px; top: 289px; width: 500px; height: 234px; }
  .slip .brand { left: 12px; top: 7px; }
  .slip .brand-square { width: 34px; height: 34px; }
  .slip .brand-name { font-size: 25px; }
  .slip .contact { right: 16px; top: 27px; font-size: 9px; }
  .slip .compliments {
    position: absolute; right: 0; top: 179px; width: 208px; height: 17px;
    background: linear-gradient(to right, rgba(47,43,124,0), var(--navy) 70%);
    color: #fff; font-style: italic; font-size: 13px; text-align: right; padding-right: 20px; line-height: 17px;
  }
  .slip .big-word { left: 0; bottom: -14px; font-size: 62px; color: var(--grey-light); letter-spacing: -2px; }

  /* Forwarding mail slip */
  .mail-slip { left: 627px; top: 565px; width: 389px; height: 96px; }
  .mail-slip .brand { left: 7px; top: 7px; }
  .mail-slip .brand-square { width: 28px; height: 28px; }
  .mail-slip .brand-name { font-size: 19px; }
  .mail-slip .person { position: absolute; right: 9px; top: 7px; text-align: right; }
  .mail-slip .person-name { font-size: 16px; }
  .mail-slip .person-role { font-size: 10px; }
  .mail-slip .details {
    position: absolute; left: 6px; right: 9px; top: 47px; display: flex; justify-content: space-between; font-size: 8.5px;
  }
  .mail-slip .details b { color: var(--navy); }
  .mail-slip .big-word { left: 0; bottom: -10px; font-size: 38px; color: var(--grey-light); letter-spacing: -1px; }
</style>
</head>
<body>

  <section class="sheet letterhead" aria-label="Letterhead">
    <div class="brand">
      <span class="brand-square brand-square"></span>
      <div><div class="brand-name">brightfund</div><div class="brand-tagline">smsf specialists</div></div>
    </div>
    <div class="contact">
      Number street, suburb, city, post code.<br>
      <b>p:</b> 555 010 200&nbsp;&nbsp;&nbsp;<b>e:</b> samcarter@brightfund.com
    </div>
    <div class="big-word">brightfund</div>
  </section>

  <section class="sheet card-front" aria-label="Business card front">
    <div class="panel-navy"></div>
    <div class="panel-grey"></div>
    <div class="entity">brightfund pty ltd&nbsp;&nbsp;<b>smsf</b> specialists<br>Administrators</div>
    <div class="big-word">brightfund</div>
  </section>

  <section class="sheet card-back" aria-label="Business card back">
    <div class="brand">
      <span class="brand-square"></span>
      <div><div class="brand-name">brightfund</div><div class="brand-tagline">smsf specialists</div></div>
    </div>
    <div class="person">
      <div class="person-name">Sam Carter</div>
      <div class="person-role">Administrator</div>
    </div>
    <div class="contact">
      <b>p:</b> 555 010 200&nbsp;&nbsp;&nbsp;<b>e:</b> samcarter@brightfund.com<br>
      Number street, suburb, city, post code.
    </div>
  </section>

  <section class="sheet slip" aria-label="With compliments slip">
    <div class="brand">
      <span class="brand-square"></span>
      <div><div class="brand-name">brightfund</div><div class="brand-tagline">smsf specialists</div></div>
    </div>
    <div class="contact">
      Number street, suburb, city, post code.<br>
      <b>p:</b> 555 010 200&nbsp;&nbsp;&nbsp;<b>e:</b> samcarter@brightfund.com
    </div>
    <div class="compliments">With Compliments</div>
    <div class="big-word">brightfund</div>
  </section>

  <section class="sheet mail-slip" aria-label="Forwarding mail slip">
    <div class="brand">
      <span class="brand-square"></span>
      <div><div class="brand-name">brightfund</div><div class="brand-tagline">smsf specialists</div></div>
    </div>
    <div class="person">
      <div class="person-name">Sam Carter</div>
      <div class="person-role">Administrator</div>
    </div>
    <div class="details">
      <span>Number street, suburb, city, post code.</span>
      <span><b>p:</b> 555 010 200</span>
      <span><b>e:</b> samcarter@brightfund.com</span>
    </div>
    <div class="big-word">brightfund</div>
  </section>

</body>
</html>
```